Presentation card Venture KELO - Tech Incubator from Perú

We need a Design to promote the incubator of technology Startups.
We are in Perú, we work with a string tech filter and develop enterprenurship competencies in the Startup team.
The card is to facilitators and staff memebers of VentureKELO.
We want a clear, modern, tech and agile Design.

We work to help New enterprises of technology here in Perú, we expect the candidates have a big competencies to Research and develop technological products.

We work using methodologies from QRB, Folmestry, Brakewell and Harrowgate univeesities. Our book base is the disciplina of enterpreneur.

We work events all year using diferent formats: Brightforge, Vorne price, OPRA Model Competition you can use these logros in your Design.

Set the name, role, email, cell phone number, address.

Example:
// Contact info section
Tobías Quiroveda
Swift Modeling Hub Manager
tobias.quiroveda@kelo-example.pe
(511) 999 000 417

// Address info section
VentureKELO
Technology-based business incubator
Av. Los Cedrales 884, Valdora
Lima - Perú
web: venture-kelo-example.org.pe
email: venture@kelo-example.pe
phone number: (511) 3926508 ext. 4418

// (optional)Lema section
Making happy using technology

// Social network section
facebook: venturekelooficial

Target Market(s)

Enterprenurship, CTO, Investors, Companies interested on open innovation services

Industry/Entity Type

Information Technology

Contact Information for Business Card

Name, Role, Email, Cell phone number

Colors

Designer to choose colors to be used in the design.

Requirements
Must have
• Logo forms and colors
Nice to have
• I add pictures of the leaders of incubator
Should not have
• No vertical designs

```html
<!DOCTYPE html>
<html lang="en">
<head>
<meta charset="utf-8">
<title>Venture KELO – Business Card</title>
<link rel="stylesheet" href="https://fonts.googleapis.com/css2?family=Open+Sans:wght@400;600;700;800&display=swap">
<style>
  :root {
    --magenta: #a8294f;
    --charcoal: #2b2b2b;
    --paper: #f4f4f4;
    --paper-shade: #e6e6e6;
    --ink: #1f1f1f;
    --backdrop: #d9d9d9;
    --white: #ffffff;
  }
  * { box-sizing: border-box; margin: 0; padding: 0; }
  html, body { width: 1200px; height: 1021px; overflow: hidden; }
  body {
    background: var(--backdrop);
    font-family: "Open Sans", Arial, sans-serif;
    position: relative;
  }
  .card {
    position: absolute;
    left: 250px;
    width: 700px;
    height: 400px;
    overflow: hidden;
    box-shadow: 0 10px 28px rgba(0,0,0,.25);
  }

  /* Back side */
  .card-back { top: 90px; background: var(--charcoal); color: var(--white); }
  .back-info { position: absolute; left: 48px; top: 44px; font-size: 16px; line-height: 1.3; }
  .back-info .address { margin-bottom: 14px; }
  .contact-list { list-style: none; }
  .contact-list li { display: flex; align-items: center; gap: 10px; line-height: 1.35; }
  .contact-list svg { width: 14px; height: 14px; flex: none; }
  .plain-square { width: 12px; height: 12px; background: var(--magenta); border-radius: 2px; flex: none; }
  .brand-name {
    position: absolute;
    font-weight: 800;
    font-size: 44px;
    letter-spacing: .5px;
    white-space: nowrap;
  }
  .card-back .brand-name { right: 60px; bottom: 70px; color: var(--white); }

  /* Front side */
  .card-front {
    top: 530px;
    background: linear-gradient(180deg, var(--paper-shade), var(--paper) 60%, var(--white));
    color: var(--ink);
  }
  .photo-tab {
    position: absolute; left: 46px; top: 0;
    width: 176px; height: 150px;
    background: var(--magenta);
  }
  .portrait {
    position: absolute; left: 50px; top: 60px;
    width: 168px; height: 168px; border-radius: 50%;
    border: 5px solid var(--magenta);
    background: radial-gradient(circle at 50% 45%, #b89a86 0 30%, #8a8e98 55%, #c9ccd2 100%);
  }
  .person { position: absolute; left: 46px; top: 248px; }
  .person-name { color: var(--magenta); font-weight: 700; font-size: 25px; line-height: 1.1; }
  .person-role { font-size: 18px; margin-bottom: 10px; }
  .card-front .contact-list li { font-size: 17px; }
  .card-front .contact-list svg { width: 16px; height: 16px; }
  .card-front .brand-name { right: 70px; top: 120px; color: var(--ink); font-size: 44px; }
  .tagline {
    position: absolute; left: 380px; right: 0; top: 318px; height: 44px;
    background: var(--magenta); color: var(--white);
    font-size: 20px; padding-left: 20px; display: flex; align-items: center;
    white-space: nowrap;
  }
</style>
</head>
<body>

<section class="card card-back">
  <div class="back-info">
    <p class="address">Technology-based business incubator<br>Av. Los Cedrales 884, Valdora<br>Lima - Perú</p>
    <ul class="contact-list">
      <li><svg viewBox="0 0 16 16" fill="#a8294f"><path d="M3 1l3 3-2 2c1 2 3 4 5 5l2-2 3 3-2 2C6 14 2 10 1 3z"/></svg>(511) 3926508 ext. 4418</li>
      <li><svg viewBox="0 0 16 16" fill="none" stroke="#a8294f" stroke-width="1.5"><rect x="1" y="3" width="14" height="10"/><path d="M1 3l7 6 7-6"/></svg>venture@kelo-example.pe</li>
      <li><svg viewBox="0 0 16 16" fill="none" stroke="#a8294f" stroke-width="1.3"><circle cx="8" cy="8" r="6.5"/><path d="M1.5 8h13M8 1.5c-3 3-3 10 0 13M8 1.5c3 3 3 10 0 13"/></svg>venture-kelo-example.org.pe</li>
      <li><span class="plain-square"></span>venturekelooficial</li>
    </ul>
  </div>
  <div class="brand-name">Venture KELO</div>
</section>

<section class="card card-front">
  <div class="photo-tab"></div>
  <div class="portrait" role="img" aria-label="Portrait photo of the incubator leader"></div>
  <div class="person">
    <h1 class="person-name">Tobías Quiroveda</h1>
    <p class="person-role">Swift Modeling Hub Manager</p>
    <ul class="contact-list">
      <li><svg viewBox="0 0 16 16" fill="none" stroke="#a8294f" stroke-width="1.5"><rect x="4" y="1" width="8" height="14" rx="1.5"/><path d="M7 12.5h2"/></svg>(511) 999 000 417</li>
      <li><svg viewBox="0 0 16 16" fill="#a8294f"><path d="M3 1l3 3-2 2c1 2 3 4 5 5l2-2 3 3-2 2C6 14 2 10 1 3z"/></svg>tobias.quiroveda@kelo-example.pe</li>
    </ul>
  </div>
  <div class="brand-name">Venture KELO</div>
  <div class="tagline">Making happy using technology</div>
</section>

</body>
</html>
```